We need a business card design for a Dubai based company .

We need a business card for a Dubai based company called "Zernova Smoking Requisites Trading LLC". We mainly import Flavoured Tobacco products and Charcoal which is used for smoking in a Hookah/Shisha and distribute to the wholesalers and retailers. Logo file is attached herewith.

```html
<!DOCTYPE html>
<html lang="en">
<head>
<meta charset="utf-8">
<title>Zernova Smoking Requisites Trading LLC – Business Card</title>
<link href="https://fonts.googleapis.com/css2?family=Arimo:wght@400;700&display=swap" rel="stylesheet">
<style>
  :root {
    --stage: #2a2a2c;
    --card-dark: #1c1c1e;
    --brand-red: #c0393d;
    --pattern-red: #b8353a;
    --ink-light: #ffffff;
    --rule: #6a6a6c;
  }
  * { box-sizing: border-box; margin: 0; padding: 0; }
  html, body {
    width: 1200px; height: 1108px; overflow: hidden;
    background: var(--stage);
    font-family: "Arimo", Arial, sans-serif;
  }
  .stage {
    position: relative; width: 1200px; height: 1108px;
    display: flex; justify-content: center; align-items: center; gap: 90px;
  }
  .card {
    width: 380px; height: 620px; border-radius: 18px;
    position: relative; overflow: hidden;
    box-shadow: 0 18px 40px rgba(0,0,0,.45);
  }
  .card-front {
    background: var(--card-dark); color: var(--ink-light);
    display: flex; flex-direction: column; align-items: center;
    padding-top: 150px; text-align: center;
  }
  .brand {
    display: flex; align-items: center; gap: 14px;
  }
  .brand-mark {
    width: 16px; height: 16px; background: var(--brand-red);
  }
  .brand-name {
    font-size: 46px; font-weight: 400; letter-spacing: 5px;
    color: var(--ink-light); line-height: 1;
  }
  .brand-tagline {
    margin-top: 14px; font-size: 10px; letter-spacing: 3.2px;
    color: var(--brand-red); text-transform: uppercase;
  }
  .person { margin-top: 110px; }
  .person-name {
    font-size: 24px; letter-spacing: 1.5px; text-transform: uppercase;
  }
  .person-role {
    margin-top: 6px; font-size: 15px; letter-spacing: 1.2px;
    color: var(--brand-red); text-transform: uppercase;
  }
  .icon-rule {
    margin-top: 18px; display: flex; align-items: center; gap: 10px; width: 290px;
  }
  .icon-rule::before, .icon-rule::after {
    content: ""; flex: 1; height: 1px; background: var(--rule);
  }
  .icon-tile {
    width: 26px; height: 26px; border-radius: 5px; background: var(--brand-red);
    display: flex; align-items: center; justify-content: center;
  }
  .icon-tile svg { width: 16px; height: 16px; }
  .contact-list {
    margin-top: 12px; list-style: none; font-size: 15px; line-height: 1.45;
    letter-spacing: .6px; text-transform: uppercase;
  }
  .divider { width: 290px; height: 1px; background: var(--rule); margin: 14px 0; }
  .address { font-size: 14px; line-height: 1.45; letter-spacing: .6px; text-transform: uppercase; }

  .card-back {
    background: linear-gradient(160deg, #c53d42 0%, var(--pattern-red) 100%);
    display: flex; justify-content: center; align-items: center;
  }
  .back-pattern {
    position: absolute; inset: 0;
    background: repeating-linear-gradient(-25deg, rgba(0,0,0,0) 0 30px, rgba(0,0,0,.05) 30px 44px);
  }
  .back-name {
    position: relative; font-size: 34px; letter-spacing: 4px;
    color: #ececec; font-weight: 400; margin-top: 120px;
  }
</style>
</head>
<body>
<main class="stage">
  <section class="card card-front" aria-label="Card front">
    <div class="brand">
      <span class="brand-mark"></span>
      <span class="brand-name">ZERNOVA</span>
    </div>
    <p class="brand-tagline">Smoking Requisites Trading LLC</p>

    <div class="person">
      <h1 class="person-name">Daniel Carter</h1>
      <p class="person-role">Managing Director</p>
    </div>

    <div class="icon-rule">
      <span class="icon-tile">
        <svg viewBox="0 0 16 16" fill="none" stroke="#1c1c1e" stroke-width="1.6">
          <path d="M4 2l2 3-1.5 1.5a8 8 0 0 0 5 5L11 10l3 2-1 2.5C7 14 2 9 1.5 3z"/>
        </svg>
      </span>
      <span class="icon-tile">
        <svg viewBox="0 0 16 16" fill="none" stroke="#1c1c1e" stroke-width="1.6">
          <rect x="2" y="4" width="12" height="8"/><path d="M2 4l6 5 6-5"/>
        </svg>
      </span>
      <span class="icon-tile">
        <svg viewBox="0 0 16 16" fill="none" stroke="#1c1c1e" stroke-width="1.4">
          <circle cx="8" cy="8" r="6"/><ellipse cx="8" cy="8" rx="2.6" ry="6"/><path d="M2 8h12"/>
        </svg>
      </span>
    </div>

    <ul class="contact-list">
      <li>044-555 010 200</li>
      <li>info@zernovatrade.com</li>
      <li>www.zernovatrade.com</li>
    </ul>
    <div class="divider"></div>
    <p class="address">421, Address Line Goes Here<br>45452, Country Name</p>
  </section>

  <section class="card card-back" aria-label="Card back">
    <div class="back-pattern" role="img" aria-label="Tonal repeating brand-name pattern in deeper red across the card"></div>
    <p class="back-name">ZERNOVA</p>
  </section>
</main>
</body>
</html>
```